Book cover (front only) for proposal by established author

We need a book cover design - must be inspirational, credible, powerful, noticeable - for a self-help book being written by an established author (15 books with major publishers). Front cover only. This will be used in a proposal being sent to a literary agent; it's NOT for publication, so high-res is NOT needed. We are providing a draft design in a doc format, but you have complete freedom with the graphics, colors, and fonts. Final product should be a pdf file, unless you have a better suggestion.

```html
<!DOCTYPE html>
<html lang="en">
<head>
<meta charset="utf-8">
<title>Who We Can Be – Book Cover</title>
<link rel="stylesheet" href="https://fonts.googleapis.com/css2?family=Open+Sans:wght@300;400&display=swap">
<style>
  :root {
    --backdrop: #2c3031;
    --paper: #eeeef0;
    --ink: #454547;
    --ink-soft: #5a5a5c;
    --accent: #1a9be0;
    --rule: #3f9fd0;
  }
  * { margin: 0; padding: 0; box-sizing: border-box; }
  html, body {
    width: 1200px;
    height: 748px;
    overflow: hidden;
    background: var(--backdrop);
    font-family: "Open Sans", Arial, sans-serif;
  }
  .cover {
    position: absolute;
    left: 364px;
    top: 42px;
    width: 472px;
    height: 630px;
    background: var(--paper);
    color: var(--ink);
    text-align: center;
  }
  .tagline {
    position: absolute;
    left: 0;
    right: 0;
    top: 44px;
    font-size: 11px;
    line-height: 18px;
    font-weight: 400;
    color: var(--ink-soft);
    text-transform: uppercase;
    white-space: nowrap;
  }
  .rule {
    position: absolute;
    left: 26px;
    width: 420px;
    height: 1px;
    background: var(--rule);
  }
  .rule--top { top: 82px; }
  .rule--bottom { top: 154px; }
  .title {
    position: absolute;
    left: 0;
    right: 0;
    top: 86px;
    font-size: 50px;
    line-height: 64px;
    font-weight: 300;
    letter-spacing: 0.5px;
    color: var(--ink);
    white-space: nowrap;
  }
  .benefits {
    position: absolute;
    left: 0;
    right: 0;
    top: 169px;
    list-style: none;
    font-size: 13px;
    line-height: 23px;
    color: var(--ink);
    text-transform: uppercase;
    white-space: nowrap;
  }
  .benefits .dot {
    display: inline-block;
    width: 9px;
    height: 9px;
    margin: 0 7px 1px;
    border-radius: 50%;
    background: var(--accent);
    vertical-align: middle;
  }
  .emblem {
    position: absolute;
    left: 160px;
    top: 331px;
    width: 141px;
    height: 141px;
  }
  .author {
    position: absolute;
    left: 0;
    right: 0;
    top: 584px;
    font-size: 22px;
    line-height: 30px;
    font-weight: 400;
    color: var(--ink-soft);
    text-transform: uppercase;
    white-space: nowrap;
  }
  .author .credential { font-size: 13px; }
  .band {
    position: absolute;
    left: 0;
    right: 0;
    bottom: 0;
    height: 9px;
    background: var(--accent);
  }
</style>
</head>
<body>
  <main class="cover">
    <p class="tagline">A pioneering behavioral scientist reveals the power<br>we all have to grow and flourish in every part of our daily lives</p>
    <div class="rule rule--top"></div>
    <h1 class="title">WHO WE CAN BE</h1>
    <div class="rule rule--bottom"></div>
    <ul class="benefits">
      <li>Happier in our relationships<span class="dot"></span>Better parents</li>
      <li>More fit<span class="dot"></span>More creative<span class="dot"></span>More motivated</li>
      <li>More calm<span class="dot"></span>And more sexually fulfilled</li>
    </ul>
    <svg class="emblem" viewBox="0 0 141 141" role="img" aria-label="Illustration of two silhouetted people facing each other with small hearts above, inside a blue circle">
      <circle cx="70.5" cy="70.5" r="70.5" fill="#1596e6"/>
    </svg>
    <p class="author">Daniel Marlowe <span class="credential">- Ph.D.</span></p>
    <div class="band"></div>
  </main>
</body>
</html>
```